Business card for international trading company
Dear Project Holder...thanks for giving me 5 star, I saw your project really in the end time, if u want any changes in this design, just let me know and I do it for u...
regards...
For #183,
Please minimize the size of the logo so you can include the arabic name. Please also use the following fonts:
http://www.pixorambe.net/photos/morlin_studio/5821904637/
Use P for the phone and F for fax. You can also mention the email and website without words like email and website before.
Please use fonts as the following:
Try also to use P for the phone and F for fax. You can also mention the email and website without words like email and website before.
I AM STILL WAITING FOR CREATIVE AND EXCLUSIVE IDEAS!
#138 might be an example of a special idea for this project, but we are expecting MOOOORE creative and wonderful designs!
LOOK AT THESE DESIGNS:
http://www.quillnovaprints.com/inspiration/minimal-business-cards/
Please let us see your creativity!
I am looking for more creative ideas which are unique and deigned especially for this project.
One thing to point out, you can exclude the fax to make more space. You can also exclude the website from the front and just include it on the back of the card.
IMPORTANT: If you think it looks good, you can make use of our slogan "Envisioning Tomorrow" to be included with the logo on the back of the card.
I am still waiting for MORE creative ideas. I uploaded the figure used in our logo as 2D. Please find it as an attachment. It might be useful.
Please refer to the following link to find very creative ideas:

```html
<!DOCTYPE html>
<html lang="en">
<head>
<meta charset="utf-8">
<title>Norvane Stationery Set</title>
<link rel="stylesheet" href="https://fonts.googleapis.com/css2?family=Montserrat:wght@700&family=Open+Sans:wght@400;600&family=Noto+Naskh+Arabic:wght@400&display=swap">
<style>
  :root {
    --stage-light: #b9b9b9;
    --stage-dark: #6a6a6a;
    --paper: #ffffff;
    --brand-ink: #46429a;
    --band-top: #2a9cc0;
    --band-bottom: #0d6a8f;
    --text-body: #4a4a4a;
    --ghost: #e9e8f3;
  }
  * { margin: 0; padding: 0; box-sizing: border-box; }
  html, body { width: 1200px; height: 626px; overflow: hidden; }
  body {
    position: relative;
    background: radial-gradient(ellipse at 50% 45%, var(--stage-light) 0%, #9b9b9b 55%, var(--stage-dark) 100%);
    font-family: "Open Sans", Arial, sans-serif;
    color: var(--text-body);
  }
  .sheet {
    position: absolute;
    background: var(--paper);
    box-shadow: 0 2px 6px rgba(0,0,0,.35);
    overflow: hidden;
  }
  .brand-band {
    position: absolute; left: 0; top: 0; width: 100%;
    background: linear-gradient(180deg, var(--band-top), var(--band-bottom));
  }
  .wordmark {
    position: absolute;
    display: flex; align-items: center; gap: 5px;
    font-family: "Montserrat", Arial, sans-serif;
    font-weight: 700;
    color: var(--brand-ink);
    letter-spacing: -0.5px;
  }
  .wordmark .dot {
    border-radius: 50%;
    background: var(--brand-ink);
    flex: none;
  }
  .ghost-circle {
    position: absolute;
    border-radius: 50%;
    background: var(--ghost);
  }
  .contact {
    position: absolute;
    font-size: 6px;
    line-height: 1.45;
  }
  .arabic {
    position: absolute;
    font-family: "Noto Naskh Arabic", serif;
    color: var(--text-body);
    direction: rtl;
  }

  /* Business card, front */
  .card-front { left: 34px; top: 259px; width: 158px; height: 96px; border-radius: 6px; }
  .card-front .wordmark { left: 16px; top: 30px; font-size: 15px; }
  .card-front .wordmark .dot { width: 17px; height: 17px; }
  .card-front .contact { left: 40px; top: 62px; font-size: 4.5px; }

  /* Business card, back */
  .card-back { left: 34px; top: 372px; width: 158px; height: 98px; border-radius: 6px; }
  .card-back .title-box {
    position: absolute; right: 0; top: 0; width: 80px; height: 19px;
    background: linear-gradient(180deg, var(--band-top), var(--band-bottom));
    color: #fff; font-size: 4.5px; line-height: 1.3; padding: 3px 6px; text-align: right;
  }
  .card-back .wordmark { left: 10px; top: 22px; font-size: 13px; }
  .card-back .wordmark .dot { width: 15px; height: 15px; }
  .card-back .contact { left: 10px; top: 52px; font-size: 4.3px; }
  .card-back .arabic { right: 12px; top: 50px; font-size: 8px; }

  /* Letterhead */
  .letterhead { left: 233px; top: 29px; width: 418px; height: 566px; }
  .letterhead .brand-band { height: 14px; }
  .letterhead .wordmark { left: 16px; top: 62px; font-size: 20px; }
  .letterhead .wordmark .dot { width: 30px; height: 30px; }
  .letterhead .ghost-circle { left: 178px; top: 288px; width: 210px; height: 210px; }
  .letterhead .contact { left: 20px; top: 516px; }

  /* Envelope, back with flap */
  .envelope-back { left: 679px; top: 79px; width: 490px; height: 221px; }
  .envelope-back .flap { position: absolute; left: 0; top: 0; }
  .envelope-back .seal {
    position: absolute; left: 226px; top: 20px; width: 38px; height: 38px;
    border-radius: 50%; background: rgba(255,255,255,.9);
  }

  /* Envelope, front */
  .envelope-front { left: 679px; top: 338px; width: 490px; height: 214px; }
  .envelope-front .brand-band { height: 17px; }
  .envelope-front .wordmark { left: 16px; top: 32px; font-size: 20px; }
  .envelope-front .wordmark .dot { width: 28px; height: 28px; }
  .envelope-front .ghost-circle { left: 320px; top: 64px; width: 120px; height: 120px; }
  .envelope-front .contact { left: 20px; top: 150px; }
</style>
</head>
<body>

  <section class="sheet card-front" aria-label="Business card front">
    <div class="wordmark"><span class="dot"></span>NORVANE</div>
    <div class="contact">www.norvane.com</div>
  </section>

  <section class="sheet card-back" aria-label="Business card back">
    <div class="title-box">Karim Haddad<br>Sales Manager</div>
    <div class="wordmark"><span class="dot"></span>NORVANE</div>
    <div class="arabic">نورفين</div>
    <div class="contact">
      P +971 4 555 0182<br>
      M +971 50 555 0419<br>
      karim@norvane.com<br>
      PO Box 4172, Dubai
    </div>
  </section>

  <section class="sheet letterhead" aria-label="Letterhead">
    <div class="brand-band"></div>
    <div class="wordmark"><span class="dot"></span>NORVANE</div>
    <div class="ghost-circle"></div>
    <div class="contact">
      www.norvane.com<br>
      P +971 4 555 0182<br>
      F +971 4 555 0183<br>
      info@norvane.com<br>
      PO Box 4172, Dubai, UAE
    </div>
  </section>

  <section class="sheet envelope-back" aria-label="Envelope back">
    <svg class="flap" width="490" height="100" viewBox="0 0 490 100">
      <defs>
        <linearGradient id="flap-fill" x1="0" y1="0" x2="0" y2="1">
          <stop offset="0" stop-color="#0d6a8f"/>
          <stop offset="1" stop-color="#2a9cc0"/>
        </linearGradient>
      </defs>
      <path d="M0 0 H490 V58 Q245 92 0 58 Z" fill="url(#flap-fill)"/>
    </svg>
    <div class="seal"></div>
  </section>

  <section class="sheet envelope-front" aria-label="Envelope front">
    <div class="brand-band"></div>
    <div class="wordmark"><span class="dot"></span>NORVANE</div>
    <div class="ghost-circle"></div>
    <div class="contact">
      www.norvane.com<br>
      P +971 4 555 0182<br>
      F +971 4 555 0183<br>
      info@norvane.com<br>
      PO Box 4172, Dubai, UAE
    </div>
  </section>

</body>
</html>
```